.

Target Market(s)

Young, male, tech savvy, cryptocurrency investors

Industry/Entity Type

Information Technology

Logo Text

.

Coding

Coded - Design and coding required

Number of Pages Required

1 page

Font styles to use
Sans Serif

Colors

Designer to choose colors to be used in the design.

Requirements
Must have
• .

```html
<!DOCTYPE html>
<html lang="en">
<head>
<meta charset="utf-8">
<title>Kryptos Grid – Airdrop</title>
<link href="https://fonts.googleapis.com/css2?family=Open+Sans:ital,wght@0,400;0,600;0,700;1,400;1,700&display=swap" rel="stylesheet">
<style>
  :root {
    --navy: #1a2e8c;
    --brand-blue: #1f56c4;
    --orange: #ff6a0d;
    --grey-text: #6b6b6b;
    --body-text: #1e1e1e;
    --rule: #b9b9b9;
    --hero-deep: #06173a;
    --hero-mid: #124a8c;
    --hero-glow: #2d7fd0;
    --white: #ffffff;
    --input-border: #b5b5b5;
  }
  * { box-sizing: border-box; margin: 0; padding: 0; }
  html, body { width: 968px; height: 1200px; overflow: hidden; background: var(--white); }
  body { font-family: "Open Sans", Arial, sans-serif; position: relative; }

  .site-header { position: absolute; left: 0; top: 0; width: 968px; height: 172px; }
  .brand { position: absolute; left: 26px; top: 30px; display: flex; align-items: center; gap: 14px; }
  .brand-dot { width: 38px; height: 38px; border-radius: 50%; background: var(--orange); }
  .brand-name { font-size: 46px; font-weight: 700; color: var(--brand-blue); letter-spacing: -0.5px; line-height: 1; }
  .tagline { position: absolute; right: 28px; top: 44px; width: 420px; text-align: center;
    font-size: 20px; font-style: italic; font-weight: 700; color: var(--grey-text); line-height: 27px; }
  .header-rule { position: absolute; left: 29px; top: 167px; width: 334px; height: 1px; background: var(--rule); }

  .hero { position: absolute; left: 0; top: 175px; width: 968px; height: 546px; overflow: hidden; }
  .hero-art { position: absolute; inset: 0;
    background: radial-gradient(ellipse at 50% 55%, var(--hero-glow) 0%, var(--hero-mid) 40%, var(--hero-deep) 100%); }
  .hero-title { position: absolute; top: 14px; width: 100%; text-align: center; color: var(--white);
    font-size: 60px; font-weight: 400; line-height: 1.2; }
  .hero-subtitle { position: absolute; top: 96px; width: 100%; text-align: center; color: var(--white);
    font-size: 33px; font-weight: 400; line-height: 1.2; }
  .slider-arrow { position: absolute; top: 256px; }
  .slider-arrow.prev { left: 14px; }
  .slider-arrow.next { right: 14px; }
  .slider-dots { position: absolute; top: 490px; left: 420px; display: flex; gap: 30px; }
  .slider-dot { width: 24px; height: 24px; border-radius: 50%; background: var(--orange); opacity: .85; }
  .slider-dot.active { border: 3px solid var(--white); opacity: 1; }

  .about { position: absolute; left: 34px; top: 748px; width: 900px; }
  .about-title { text-align: center; font-size: 30px; font-weight: 700; color: var(--navy); line-height: 44px; }
  .about-text { margin-top: 12px; font-size: 21.5px; line-height: 37.5px; color: var(--body-text); }

  .signup { position: absolute; left: 34px; top: 1106px; width: 900px; height: 60px; display: flex; align-items: center; }
  .signup-label { font-size: 28px; font-weight: 700; color: var(--navy); width: 189px; white-space: nowrap; }
  .signup-input { width: 430px; height: 56px; border: 2px solid var(--input-border); padding: 0 16px;
    display: flex; align-items: center; font-size: 19px; font-style: italic; color: #333; }
  .signup-button { margin-left: 27px; width: 220px; height: 58px; background: var(--orange); color: var(--white);
    font-size: 27px; font-weight: 700; display: flex; align-items: center; justify-content: center; white-space: nowrap; }
</style>
</head>
<body>
  <header class="site-header">
    <div class="brand">
      <span class="brand-dot"></span>
      <span class="brand-name">Kryptos.grid</span>
    </div>
    <p class="tagline">The World's Most Advanced Blockchain and the Widest Token Distribution</p>
    <div class="header-rule"></div>
  </header>

  <section class="hero">
    <div class="hero-art" role="img" aria-label="Night city skyline with glowing binary code and three computer monitors on a desk"></div>
    <h1 class="hero-title">October 2017</h1>
    <h2 class="hero-subtitle">Coreline Network Linked Address Airdrop</h2>
    <svg class="slider-arrow prev" width="20" height="34" viewBox="0 0 20 34" aria-label="Previous slide">
      <polygon points="18,2 2,17 18,32" fill="#ffffff"/>
    </svg>
    <svg class="slider-arrow next" width="20" height="34" viewBox="0 0 20 34" aria-label="Next slide">
      <polygon points="2,2 18,17 2,32" fill="#ffffff"/>
    </svg>
    <div class="slider-dots">
      <span class="slider-dot"></span>
      <span class="slider-dot active"></span>
      <span class="slider-dot"></span>
    </div>
  </section>

  <section class="about">
    <h3 class="about-title">About Kryptos Grid</h3>
    <p class="about-text">Lorem Ipsum is simply dummy text of the printing and typesetting industry. Lorem Ipsum has been the industry's standard dummy text ever since the 1500s, when an unknown printer took a galley of type and scrambled it to make a type specimen book. It has survived not only five centuries, but also the leap into electronic typesetting, remaining essentially unchanged. It was popularised in the 1960s with the release of Setwell sheets containing Lorem Ipsum passages, and more recently with desktop publishing software like Quill PageForge including versions of Lorem Ipsum.</p>
  </section>

  <section class="signup">
    <span class="signup-label">Get Updates:</span>
    <div class="signup-input">Your email</div>
    <div class="signup-button">Sign-up Now</div>
  </section>
</body>
</html>
```